Social Media Beitrag (Stelle)
Alles perfekt, sehr unkomplizierte Zusammenarbeit. Schnell ein passendes Design gefunden. Die Vorstellungen wurden super entgegengenommen und umgesetzt.
Zielgruppe
Wir sind eine allgemeinmedizinischen Tierklinik, welche Unterstützung im Team sucht. Aus diesem Grund ist die Zielgruppe bei dieser Arbeit potentielle Mitarbeiter.
Aufgabenstellung
Wir möchten gerne einen Social-Media-Beitrag beispielsweise auf Pixelbrunn und Kontaktwand machen und deshalb das Stelleninserat (im Anhang) in anderer verkürzter ansprechender Art darstellen. Ich stelle mir vor die Message auf ca. 3-4 quadratischen Bilder darzustellen, dass der Leser diese nacheinander ansehen kann und direkt angesprochen wird. Es muss nicht alles vom Stelleninserat mit eingebaut werden, sondern nur das wichtigste. Bei Pixelbrunn wäre ideale Größe für quadratische Posts ist 1080 px x 1080 px mit einem Seitenverhältnis von 1:1. Wir sind jedoch für andere Ideen offen oder wenn ihr auch das Gefühl habt wir packen die Message auf ein Bild. Ziel ist es möglichst ein breites Publikum online ansprechen zu können. Das Corporate Design der Unternehmung sollte auch mit berücksichtigt werden. Das Design sollte im Indesign oder Photoshop erstellt werden, damit wir es selbständig überarbeiten oder erweitern können.
Ich möchte keine BildVorrat-Personen auf den Post abbilden, dass wirkt zu künstlich, da es nicht die richtigen Mitarbeiter sind. Vielleicht kann auch etwas mit wenig Bild oder gar kein Bild und einfach einem Icon dargestellt werden.

```html
<!DOCTYPE html>
<html lang="de">
<head>
<meta charset="utf-8">
<title>Stelleninserat Beitrag – Lindmatt Tierärzte</title>
<link rel="stylesheet" href="https://fonts.googleapis.com/css2?family=Source+Sans+3:ital,wght@0,400;0,600;0,700;1,600&display=swap">
<style>
  :root {
    --brand-red: #d7141b;
    --ink: #1c1c1c;
    --page: #f6f6f6;
    --card: #ffffff;
    --art-warm: #c78b6e;
    --art-light: #f7e4e2;
  }
  * { box-sizing: border-box; margin: 0; padding: 0; }
  html, body { width: 1000px; height: 1200px; overflow: hidden; }
  body {
    background: var(--page);
    font-family: "Source Sans 3", sans-serif;
    color: var(--ink);
    position: relative;
  }
  .post {
    position: absolute;
    width: 480px; height: 480px;
    background: var(--card);
    box-shadow: 0 2px 10px rgba(0,0,0,0.08);
    overflow: hidden;
  }
  .post-intro   { left: 13px;  top: 113px; }
  .post-job     { left: 507px; top: 113px; }
  .post-contact { left: 260px; top: 607px; }

  .accent { color: var(--brand-red); }
  .rule {
    position: absolute;
    height: 3px;
    background: var(--brand-red);
    top: 430px;
  }

  /* Post 1 – Einstieg */
  .post-intro .hook {
    position: absolute; left: 32px; top: 48px; width: 420px;
    font-size: 25px; font-weight: 600; line-height: 1.16;
  }
  .post-intro .wordmark {
    position: absolute; left: 32px; top: 412px;
    font-size: 15px; font-weight: 600; line-height: 1.1;
    color: var(--brand-red);
    letter-spacing: 0.06em; text-transform: uppercase;
  }
  .post-intro .rule { left: 156px; right: 0; }

  /* Post 2 – Stelle */
  .post-job .lead {
    position: absolute; left: 32px; top: 48px;
    font-size: 17px; font-weight: 600;
  }
  .post-job .job-title {
    position: absolute; left: 32px; top: 72px;
    font-size: 21px; font-weight: 700; color: var(--brand-red);
    white-space: nowrap;
  }
  .post-job .sections {
    position: absolute; left: 32px; top: 116px; width: 240px;
  }
  .post-job h3 {
    font-size: 16px; font-weight: 600; font-style: italic;
    color: var(--brand-red); margin-top: 8px; margin-bottom: 2px;
  }
  .post-job p { font-size: 12.5px; line-height: 1.5; }
  .post-job .reception-art {
    position: absolute; left: 284px; top: 292px;
    width: 166px; height: 166px;
    background: linear-gradient(160deg, var(--art-light) 0%, var(--art-light) 45%, var(--art-warm) 100%);
    border-radius: 4px;
  }
  .post-job .rule-left { left: 0; width: 258px; }
  .post-job .rule-right { right: 0; width: 14px; }

  /* Post 3 – Kontakt */
  .post-contact .call {
    position: absolute; left: 32px; top: 50px;
    font-size: 30px; font-weight: 600; color: var(--brand-red);
    letter-spacing: 0.02em; line-height: 1;
  }
  .post-contact .sub {
    position: absolute; left: 32px; top: 86px;
    font-size: 17px; font-weight: 600;
  }
  .post-contact .contact {
    position: absolute; left: 294px; top: 366px; width: 180px;
    white-space: nowrap;
  }
  .post-contact .contact h3 {
    font-size: 16px; font-weight: 600; font-style: italic;
    color: var(--brand-red); margin-bottom: 4px;
  }
  .post-contact .contact p { font-size: 12.5px; line-height: 1.5; }
  .post-contact .rule { left: 0; width: 276px; }
</style>
</head>
<body>
  <section class="post post-intro">
    <h1 class="hook">Sind Sie auf der Suche nach einem <span class="accent">abwechslungsreichen</span> und <span class="accent">verantwortungsvollen Job?</span></h1>
    <div class="wordmark">Lindmatt<br>Tierärzte</div>
    <div class="rule"></div>
  </section>

  <section class="post post-job">
    <p class="lead">Wir suchen ab sofort eine/n engagierte/n</p>
    <h2 class="job-title">Mitarbeiter/in Empfang TPA (80-100%)</h2>
    <div class="sections">
      <h3>Anforderung :</h3>
      <p>Bevorzugt wird eine belastbare aufgestellte Persönlichkeit, welche den Kontakt mit Kunden schätzt und bereits Erfahrung im Umfeld mit Tieren mitbringt.</p>
      <h3>Stellenbeschreibung :</h3>
      <p>Sie betreuen unsere Kunden am Telefon sowie am Empfang und leisten allgemeine administrative Arbeiten.</p>
      <h3>Benefit :</h3>
      <p>Wir bieten Ihnen eine abwechslungsreiche, klar geregelte Arbeit in einem motivierten jungen Team.</p>
    </div>
    <div class="rule rule-left"></div>
    <div class="rule rule-right"></div>
    <div class="reception-art" role="img" aria-label="Illustration: Mitarbeiterin am Empfangstresen mit Computer und Pflanze"></div>
  </section>

  <section class="post post-contact">
    <h2 class="call">INTERESSIERT ?</h2>
    <p class="sub">Wir freuen uns auf Ihre Bewerbung.</p>
    <div class="contact">
      <h3>Kontakt:</h3>
      <p>Lindmatt Tierärzte, Kleintier AG<br>Talackerweg 7<br>6430 Seewil</p>
    </div>
    <div class="rule"></div>
  </section>
</body>
</html>
```